Revamp Of Landing Page For an Automated AI Voice Agents Agency

here is my current landing page https://app.brightfunnelstudio.example/v2/preview/KXWQPmR4hLsDnTfYvJcA?notrack=true

Please use all my current content and imagery of ai agents in your new design. Make it easy to ready, easy to navigate and easy to understand

I am looking for a SLEEK shiny polished looking website. I like Dark themed sites but am open to see light themed sites too so please dont be shy.

The site should have an Ai Voice Agent Theme about it. Maybe look and feel of futureistic but simple and not intimidating to the average person...

Here are a couple website designs I like for reference:
https://q4t.example/
https://ai-bots.mervinholt.example/
https://chatvexo.example/ai-agents

Target Market(s)

b2b

Industry/Entity Type

AI Voice Agents

Coding

Coded - Design and coding required

Font styles to use
Other font styles liked:
• open

Requirements
Must have
• all elements and content and images used in existing design.
Nice to have
• open
Should not have
• open

```html
<!DOCTYPE html>
<html lang="en">
<head>
<meta charset="utf-8">
<title>AI Voice Agents</title>
<link rel="stylesheet" href="https://fonts.googleapis.com/css2?family=Inter:wght@400;500;600;700;800&display=swap">
<style>
  :root {
    --bg: #0a0e15;
    --card-bg: #10151e;
    --card-border: #1c2330;
    --text: #f3f5f8;
    --text-soft: #c9cfd8;
    --text-muted: #a3abb7;
    --accent: #2e9ff0;
    --accent-light: #4fb7f7;
    --link: #36c3ef;
    --tick: #3aa8e8;
    --star: #f4b52c;
    --step-bg: #181e29;
  }
  * { box-sizing: border-box; margin: 0; padding: 0; }
  html, body { width: 800px; height: 1200px; overflow: hidden; }
  body {
    background: radial-gradient(ellipse at 75% 10%, #141b27 0%, var(--bg) 55%);
    color: var(--text);
    font-family: "Inter", sans-serif;
    position: relative;
  }
  .page { position: relative; width: 800px; height: 1200px; overflow: hidden; }

  .hero-title {
    position: absolute; left: 74px; top: 52px;
    font-size: 42px; font-weight: 800; line-height: 1.05; letter-spacing: -0.5px;
    text-transform: uppercase;
  }
  .hero-sub {
    position: absolute; left: 74px; top: 153px;
    font-size: 16px; line-height: 1.55; color: var(--text-soft);
  }
  .hero-cta {
    position: absolute; left: 74px; top: 223px;
    width: 224px; height: 44px; border-radius: 5px;
    background: linear-gradient(180deg, var(--accent-light), var(--accent));
    color: #fff; font-size: 14px; font-weight: 700; text-transform: uppercase;
    display: flex; align-items: center; justify-content: center;
    box-shadow: 0 4px 18px rgba(46,159,240,.35);
  }
  .hero-visual {
    position: absolute; left: 450px; top: 0; width: 280px; height: 340px;
    border-radius: 0 0 140px 140px;
    background: radial-gradient(ellipse at 50% 35%, #d9dee6 0%, #8b95a4 35%, #2a3240 70%, transparent 100%);
    opacity: .9;
  }

  .agent-cards {
    position: absolute; left: 73px; top: 345px;
    display: flex; gap: 11px;
  }
  .agent-card {
    width: 155px; height: 266px;
    background: var(--card-bg); border: 1px solid var(--card-border); border-radius: 6px;
    padding: 16px 12px 0 12px;
  }
  .agent-visual {
    width: 80px; height: 104px; margin: 0 auto 16px;
    border-radius: 40px 40px 20px 20px;
    background: radial-gradient(ellipse at 50% 35%, #e8ecf1 0%, #9aa3b0 55%, #2a3240 100%);
  }
  .agent-name { font-size: 15px; font-weight: 700; text-align: center; line-height: 1.25; margin-bottom: 12px; }
  .agent-desc { font-size: 11.5px; line-height: 1.55; color: var(--text-muted); margin-bottom: 12px; padding-left: 10px; }
  .agent-link { font-size: 12.5px; color: var(--link); text-decoration: none; padding-left: 10px; }

  .why { position: absolute; left: 74px; top: 652px; }
  .section-title { font-size: 25px; font-weight: 800; line-height: 1.2; text-transform: uppercase; letter-spacing: -0.3px; }
  .why-list { list-style: none; margin-top: 16px; }
  .why-list li { font-size: 16.5px; color: var(--text-soft); display: flex; align-items: center; gap: 8px; height: 32px; }
  .why-list svg { flex: none; }

  .testimonial { position: absolute; left: 428px; top: 660px; width: 310px; }
  .quote { font-size: 18.5px; line-height: 1.35; color: var(--text-soft); }
  .author { margin-top: 14px; font-size: 17px; font-weight: 700; }
  .role { font-size: 12px; color: var(--text-muted); margin-top: 4px; }
  .stars { display: flex; gap: 3px; margin-top: 12px; }

  .how { position: absolute; left: 74px; top: 902px; width: 660px; }
  .steps { position: relative; margin-top: 30px; height: 80px; }
  .step { position: absolute; top: 0; display: flex; gap: 12px; }
  .step-num {
    width: 28px; height: 28px; border-radius: 50%; background: var(--step-bg);
    font-size: 13px; display: flex; align-items: center; justify-content: center; flex: none;
  }
  .step-title { font-size: 17px; font-weight: 700; line-height: 28px; }
  .step-text { font-size: 12.5px; line-height: 1.55; color: var(--text-muted); margin-top: 8px; width: 150px; }

  .faq { position: absolute; left: 74px; top: 1093px; width: 660px; }
  .faq-grid { position: relative; margin-top: 22px; }
  .faq-item { position: absolute; top: 0; width: 320px; }
  .faq-q { font-size: 17px; font-weight: 600; }
  .faq-a { font-size: 13px; color: var(--text-muted); margin-top: 14px; white-space: nowrap; }
</style>
</head>
<body>
<div class="page">
  <header class="hero">
    <h1 class="hero-title">Meet your 24/7<br>AI voice agents</h1>
    <p class="hero-sub">Answering Calls, Booking Appointments.<br>Sending Emails &amp; More—All Day, Every.</p>
    <a class="hero-cta">Get your free demo now</a>
    <div class="hero-visual" role="img" aria-label="Illustration of a white robot voice agent wearing a headset"></div>
  </header>

  <section class="agent-cards">
    <article class="agent-card">
      <div class="agent-visual" role="img" aria-label="Robot receptionist illustration"></div>
      <h3 class="agent-name">AI Receptionist</h3>
      <p class="agent-desc">Handles overflow<br>and after-hours<br>calls instantly</p>
      <a class="agent-link">Learn more</a>
    </article>
    <article class="agent-card">
      <div class="agent-visual" role="img" aria-label="Robot lead qualifier illustration"></div>
      <h3 class="agent-name">AI Lead Qualifier</h3>
      <p class="agent-desc">Engage prospects,<br>gather and email<br>leads, easily</p>
      <a class="agent-link">Learn more</a>
    </article>
    <article class="agent-card">
      <div class="agent-visual" role="img" aria-label="Robot sales agent illustration"></div>
      <h3 class="agent-name">AI Sales Agent</h3>
      <p class="agent-desc">Provides detailed<br>information, answers<br>questions, leads</p>
      <a class="agent-link">Learn more</a>
    </article>
    <article class="agent-card">
      <div class="agent-visual" role="img" aria-label="Robot appointment setter illustration"></div>
      <h3 class="agent-name">AI Appointment<br>Setter</h3>
      <p class="agent-desc">Sends appointments<br>automatically</p>
      <a class="agent-link">Learn more</a>
    </article>
  </section>

  <section class="why">
    <h2 class="section-title">Why choose our<br>AI voice agents?</h2>
    <ul class="why-list">
      <li><svg width="11" height="11" viewBox="0 0 12 12"><path d="M2 6.5l2.5 2.5L10 3" fill="none" stroke="var(--tick)" stroke-width="1.6"/></svg>Operate 24/7 without breaks</li>
      <li><svg width="11" height="11" viewBox="0 0 12 12"><path d="M2 6.5l2.5 2.5L10 3" fill="none" stroke="var(--tick)" stroke-width="1.6"/></svg>Instantly trained using website content</li>
      <li><svg width="11" height="11" viewBox="0 0 12 12"><path d="M2 6.5l2.5 2.5L10 3" fill="none" stroke="var(--tick)" stroke-width="1.6"/></svg>Human-like sound</li>
      <li><svg width="11" height="11" viewBox="0 0 12 12"><path d="M2 6.5l2.5 2.5L10 3" fill="none" stroke="var(--tick)" stroke-width="1.6"/></svg>Cost-effective compared to traditional staffing</li>
    </ul>
  </section>

  <aside class="testimonial">
    <p class="quote">“After integrating the AI Voice Agent, our customer engagement skyrocketed!”</p>
    <p class="author">Jora Dale</p>
    <p class="role">CEO, Tecklora</p>
    <div class="stars">
      <svg width="18" height="17" viewBox="0 0 24 23"><path d="M12 1l3.1 6.9 7.4.7-5.6 5 1.7 7.4L12 17.2 5.4 21l1.7-7.4-5.6-5 7.4-.7z" fill="var(--star)"/></svg>
      <svg width="18" height="17" viewBox="0 0 24 23"><path d="M12 1l3.1 6.9 7.4.7-5.6 5 1.7 7.4L12 17.2 5.4 21l1.7-7.4-5.6-5 7.4-.7z" fill="var(--star)"/></svg>
      <svg width="18" height="17" viewBox="0 0 24 23"><path d="M12 1l3.1 6.9 7.4.7-5.6 5 1.7 7.4L12 17.2 5.4 21l1.7-7.4-5.6-5 7.4-.7z" fill="var(--star)"/></svg>
      <svg width="18" height="17" viewBox="0 0 24 23"><path d="M12 1l3.1 6.9 7.4.7-5.6 5 1.7 7.4L12 17.2 5.4 21l1.7-7.4-5.6-5 7.4-.7z" fill="var(--star)"/></svg>
      <svg width="18" height="17" viewBox="0 0 24 23"><path d="M12 1l3.1 6.9 7.4.7-5.6 5 1.7 7.4L12 17.2 5.4 21l1.7-7.4-5.6-5 7.4-.7z" fill="var(--star)"/></svg>
    </div>
  </aside>

  <section class="how">
    <h2 class="section-title">How it works</h2>
    <div class="steps">
      <div class="step" style="left:0">
        <span class="step-num">1</span>
        <div><h4 class="step-title">Sign Up</h4><p class="step-text">Provide basic information.</p></div>
      </div>
      <div class="step" style="left:237px">
        <span class="step-num">2</span>
        <div><h4 class="step-title">Customization</h4><p class="step-text">We tailor your AI agent to your business needs.</p></div>
      </div>
      <div class="step" style="left:453px">
        <span class="step-num">3</span>
        <div><h4 class="step-title">Deployment</h4><p class="step-text">Your AI agent goes live and operational.</p></div>
      </div>
    </div>
  </section>

  <section class="faq">
    <h2 class="section-title">FAQ</h2>
    <div class="faq-grid">
      <div class="faq-item" style="left:0">
        <h4 class="faq-q">What are AI Voice Agents?</h4>
        <p class="faq-a">AI powered bots that perform your conversations</p>
      </div>
      <div class="faq-item" style="left:334px">
        <h4 class="faq-q">How quickly can I get started?</h4>
        <p class="faq-a">Your customized AI agent can be live in minutes</p>
      </div>
    </div>
  </section>
</div>
</body>
</html>
```